Webdesign for blog, vlog and website
The designs for my website were better than what I expected when I started this contest. I knew I needed a call-to-action on my homepage, but I thought it wouldn't be possible and I didn't ask for it either. But Anselmo did it anyway. Furthermore, his design looked very good. For that reason I selected him as winner already before I should. I am very happy.

```html
<!DOCTYPE html>
<html lang="en">
<head>
<meta charset="utf-8">
<title>Thinkora – About</title>
<link rel="stylesheet" href="https://fonts.googleapis.com/css2?family=Roboto:wght@400;500;700&family=Bebas+Neue&display=swap">
<style>
:root{
  --navy:#1f3f66;
  --dark:#1f2329;
  --orange:#f5a623;
  --yellow:#f7c928;
  --pale:#fde07a;
  --ink:#2a2a2a;
  --white:#ffffff;
  --link:#3b6fe0;
}
*{margin:0;padding:0;box-sizing:border-box}
html,body{width:888px;height:1200px;overflow:hidden;background:var(--white)}
body{position:relative;font-family:'Roboto',sans-serif;color:var(--ink)}
.abs{position:absolute}
.topbar{left:0;top:0;width:888px;height:26px;background:var(--navy);overflow:hidden}
.topbar svg{position:absolute;left:0;top:0}
.btn-top{top:6px;height:16px;background:var(--orange);color:var(--white);font-size:8px;display:flex;align-items:center;justify-content:center;border-radius:1px}
.login{left:720px;width:42px}
.register{left:766px;width:49px}
.caret{left:837px;top:11px;width:0;height:0;border-left:3.5px solid transparent;border-right:3.5px solid transparent;border-top:4px solid var(--dark)}
.flag{left:848px;top:4px;width:25px;height:17px;display:flex;flex-direction:column}
.flag span{flex:1}
.navbar{left:0;top:26px;width:888px;height:41px;background:var(--dark)}
.brand{left:14px;top:13px;display:flex;align-items:center;gap:4px;color:var(--white);font-size:15px;font-weight:700}
.brand i{width:10px;height:10px;border-radius:50%;background:var(--white);display:block}
.nav-item{top:13px;display:flex;align-items:center;gap:6px;color:var(--white);font-size:9px;font-weight:700;height:15px}
.nav-item svg{width:15px;height:15px}
.tab{height:22px;background:var(--dark);color:var(--white);font-size:8px;font-weight:700;display:flex;align-items:center;padding-left:8px;clip-path:polygon(0 0,70% 0,100% 100%,0 100%)}
.about-tab{left:231px;top:81px;width:68px}
.blog-tab{left:230px;top:431px;width:116px;padding-left:8px;clip-path:polygon(0 0,82% 0,100% 100%,0 100%)}
.content{left:233px;width:398px;font-size:7.8px;line-height:10.1px}
.content h2{font-size:7.6px;font-weight:700;margin-left:1px}
.cta{height:20px;background:var(--dark);color:var(--white);border-radius:2px;display:flex;align-items:center;gap:5px;padding-left:7px;font-size:8.8px;font-weight:700;width:89px}
.cta svg{width:13px;height:12px}
.blog-card{left:230px;top:463px;width:288px;height:173px}
.blog-photo{position:absolute;inset:0;background:linear-gradient(160deg,#2b2a28 0%,#3a3833 45%,#8c8776 65%,#4a4640 100%)}
.blog-caption{position:absolute;left:0;right:0;bottom:0;height:45px;background:rgba(24,24,24,.93);padding:5px 0 0 10px;font-family:'Bebas Neue',sans-serif}
.blog-caption .kicker{color:var(--orange);font-size:13px;line-height:13px}
.blog-caption .title{color:var(--white);font-size:20px;line-height:20px;margin-top:2px}
.credit{left:300px;top:638px;width:218px;text-align:right;font-size:4.3px;color:#555}
.credit a{color:var(--link);text-decoration:none}
.footer{left:0;top:1066px;width:888px;height:134px;background:var(--dark);color:var(--white)}
.company{left:31px;top:36px;font-size:7.8px;line-height:12.5px}
.company strong{display:block;font-size:11px;font-weight:500;line-height:14px;margin-bottom:0}
.newsletter-label{left:342px;top:39px;font-size:7.8px}
.email{left:340px;top:53px;width:144px;height:25px;background:#050505;border-radius:2px;color:var(--white);font-size:11px;font-weight:500;display:flex;align-items:center;padding-left:7px}
.subscribe{left:489px;top:56px;width:47px;height:19px;background:var(--orange);color:var(--dark);font-size:7px;font-weight:700;display:flex;align-items:center;justify-content:center;border-radius:1px}
.legal{left:0;width:888px;top:116px;text-align:center;font-size:6.8px}
</style>
</head>
<body>
<header>
  <div class="abs topbar">
    <svg width="888" height="26" viewBox="0 0 888 26">
      <polygon points="237,0 330,0 355,26 262,26" fill="#f5a623"/>
      <polygon points="330,0 415,0 440,26 355,26" fill="#f7d24a"/>
      <polygon points="415,0 483,0 508,26 440,26" fill="#f2c42a"/>
      <polygon points="483,0 555,0 591,26 508,26" fill="#fde07a"/>
    </svg>
  </div>
  <div class="abs btn-top login">LOGIN</div>
  <div class="abs btn-top register">REGISTER</div>
  <div class="abs caret"></div>
  <div class="abs flag"><span style="background:#f5a623"></span><span style="background:#fff"></span><span style="background:#2e6fe0"></span></div>

  <nav class="abs navbar">
    <div class="abs brand"><i></i>Thinkora</div>
    <div class="abs nav-item" style="left:296px">
      <svg viewBox="0 0 16 16"><path d="M8 1 1 7.5h2V15h4v-4h2v4h4V7.5h2z" fill="#f5a623"/></svg>BLOG</div>
    <div class="abs nav-item" style="left:378px">
      <svg viewBox="0 0 16 16"><ellipse cx="6" cy="6.5" rx="5.5" ry="4" fill="#f5a623"/><ellipse cx="10.5" cy="9.5" rx="5" ry="3.7" fill="#f5a623"/><path d="M2 9 1 13l4-2z" fill="#f5a623"/></svg>FORUM</div>
    <div class="abs nav-item" style="left:458px">
      <svg viewBox="0 0 16 16"><path d="M1 6h14l-2 9H3z" fill="#f5a623"/><path d="M5 6a3 3 0 0 1 6 0" stroke="#f5a623" stroke-width="1.5" fill="none"/></svg>SHOP</div>
    <div class="abs nav-item" style="left:524px">
      <svg viewBox="0 0 16 16"><circle cx="8" cy="8" r="7.5" fill="#f5a623"/><path d="M5.8 6a2.2 2.2 0 1 1 3 2c-.6.3-.8.7-.8 1.5" stroke="#1f2329" stroke-width="1.6" fill="none"/><circle cx="8" cy="12" r="1" fill="#1f2329"/></svg>ABOUT</div>
  </nav>
</header>

<main>
  <div class="abs tab about-tab">ABOUT</div>

  <section class="abs content" style="top:112px">
    <h2>Thinkora: What are your ideas?</h2>
    <p style="margin-top:5px">Do you recognize the following situation? Someone says something to you and you think: "That is crazy! How can one think something like that?" People sometimes believe the strangest things. And even more strange is that such a person is just as convinced about his/her opinions than you are about yours! How is that possible? How come do they think like that? This is what I want to find out on the basis of news stories.</p>
    <p style="margin-top:10px">The slogan 'What are your ideas?' is applicable to everyone. If you hear or read a strange statement in a news report, you can ask yourself: what are the ideas behind this statement? But you can also ask yourself: Why do I think that this statement is strange? What are my ideas?</p>
    <p style="margin-top:10px">Does this sound difficult? Follow the blog 'Questioning remarkable statements in the news' and the vlog 'Let's look at the news from a different perspective' and you'll start to recognize underlying ideas better and better.</p>
    <p style="margin-top:10px">And of course I'm curious about your ideas too. So leave a comment below the blog, vlog or forum and we can learn more and more from each other.</p>
  </section>

  <div class="abs cta" style="left:233px;top:277px">
    <svg viewBox="0 0 13 12"><path d="M0 0h13v8H4l-3 4V8H0z" fill="#f5a623"/></svg>DISCUSS THIS</div>

  <section class="abs content" style="top:311px">
    <h2>Webshop: Share your opinion with a telling symbol or text</h2>
    <p style="margin-top:5px">In the webshop you'll find products with all kinds of ideas in the form of a text or well-known symbol. Nice for yourself or to give away as a present.</p>
    <p style="margin-top:10px">These products come from wholesalers that pay attention to the circumstances in which these products were made.</p>
  </section>

  <div class="abs cta" style="left:233px;top:388px;gap:7px;padding-left:8px">
    <svg viewBox="0 0 13 12"><path d="M0 4h13l-2 8H2z" fill="#f5a623"/><path d="M4 4a2.5 2.5 0 0 1 5 0" stroke="#f5a623" stroke-width="1.3" fill="none"/></svg>ONLINESHOP</div>

  <div class="abs tab blog-tab">VISIT THE BLOG</div>

  <article class="abs blog-card">
    <div class="blog-photo" role="img" aria-label="Photo of an open book with the word IDEA cut from printed pages standing up"></div>
    <div class="blog-caption">
      <div class="kicker">THINKORA</div>
      <div class="title">DISCOVER: THE IDEAS BEHIND THE BLOG</div>
    </div>
  </article>
  <div class="abs credit"><a>Photo</a> by rkmn / <a>CC BY</a></div>
</main>

<footer class="abs footer">
  <div class="abs company">
    <strong>Thinkora</strong>
    Chamber of commerce: 70012345<br>
    VAT number: NL000111222B01<br>
    Email: info@thinkora.nl<br>
    Phone: +31 (0)6-55501234
  </div>
  <div class="abs newsletter-label">Yes, I would like to receive the monthly Thinkora newsletter</div>
  <div class="abs email">E-Mail</div>
  <div class="abs subscribe">SUBSCRIBE</div>
  <div class="abs legal">User agreement | Privacy Policy | Terms of Service</div>
</footer>
</body>
</html>
```